Business Card for a Wedding Films Business

We require a business card design for our business 'Lewis Marrow Wedding Films'. The logo needs to look classy and high end.

Target Market(s)

Wedding Couples

Contact Information for Business Card

Lewis Marrow Wedding Films
07312 605 227
films@lewismarrowreels.com
www.lewismarrowreels.com

Facebook: @lewismarrowweddingfilms
Instagram: @lewismarrowfilms

Font styles to use
Sans Serif

Requirements
Must have
• Social media icons - Facebook and Instagram

```html
<!DOCTYPE html>
<html lang="en">
<head>
<meta charset="utf-8">
<title>Lewis Marrow Wedding Films – Business Card</title>
<link href="https://fonts.googleapis.com/css2?family=Jost:wght@400;500&display=swap" rel="stylesheet">
<style>
  :root {
    --backdrop: #2b2b2d;
    --card: #121212;
    --gold: #d4a933;
    --ink: #f2f2f2;
  }
  * { box-sizing: border-box; margin: 0; padding: 0; }
  html, body {
    width: 1200px; height: 1000px; overflow: hidden;
    background: var(--backdrop);
    font-family: "Jost", sans-serif;
  }
  .sheet {
    width: 1200px; height: 1000px;
    display: flex; flex-direction: column; align-items: center; justify-content: center;
    gap: 40px;
  }
  .card {
    position: relative;
    width: 770px; height: 440px;
    background: var(--card);
    border-radius: 26px;
    box-shadow: 0 18px 40px rgba(0,0,0,.45);
    overflow: hidden;
  }

  /* Front */
  .card--front { display: flex; align-items: center; justify-content: center; }
  .lockup { display: flex; flex-direction: column; align-items: center; color: var(--gold); font-weight: 500; }
  .lockup__mark { width: 70px; height: 70px; border: 4px solid var(--gold); margin-bottom: 26px; }
  .lockup__name { font-size: 44px; letter-spacing: .32em; margin-right: -.32em; line-height: 1; white-space: nowrap; }
  .lockup__tag { font-size: 19px; letter-spacing: .55em; margin-right: -.55em; margin-top: 12px; white-space: nowrap; }

  /* Back */
  .identity {
    position: absolute; left: 60px; top: 72px;
    display: flex; flex-direction: column; align-items: center;
    color: var(--gold); font-weight: 500;
  }
  .identity__name { font-size: 28px; letter-spacing: .28em; margin-right: -.28em; line-height: 1; white-space: nowrap; }
  .identity__tag { font-size: 13px; letter-spacing: .55em; margin-right: -.55em; margin-top: 10px; white-space: nowrap; }

  .contacts {
    position: absolute; left: 60px; top: 196px;
    list-style: none; display: flex; flex-direction: column; gap: 15px;
  }
  .contact { display: flex; align-items: center; gap: 14px; color: var(--ink); font-size: 21px; font-weight: 400; line-height: 1.2; white-space: nowrap; }
  .contact__icon { width: 22px; height: 22px; flex: none; color: var(--gold); }

  .emblem {
    position: absolute; right: 60px; top: 72px; width: 210px;
    display: flex; flex-direction: column; align-items: center; gap: 22px;
    color: var(--gold); font-weight: 500;
  }
  .emblem__mark { width: 120px; height: 120px; border: 6px solid var(--gold); }
  .emblem__name { font-size: 30px; letter-spacing: .2em; margin-right: -.2em; line-height: 1.3; text-align: center; }
</style>
</head>
<body>
<main class="sheet">
  <section class="card card--front" aria-label="Business card front">
    <div class="lockup">
      <div class="lockup__mark"></div>
      <div class="lockup__name">LEWIS MARROW</div>
      <div class="lockup__tag">WEDDING FILMS</div>
    </div>
  </section>

  <section class="card card--back" aria-label="Business card back">
    <div class="identity">
      <div class="identity__name">LEWIS MARROW</div>
      <div class="identity__tag">WEDDING FILMS</div>
    </div>

    <ul class="contacts">
      <li class="contact">
        <svg class="contact__icon" viewBox="0 0 24 24" aria-hidden="true"><path fill="currentColor" d="M6.6 10.8a15 15 0 0 0 6.6 6.6l2.2-2.2a1 1 0 0 1 1-.25 11.4 11.4 0 0 0 3.6.57 1 1 0 0 1 1 1V20a1 1 0 0 1-1 1A17 17 0 0 1 3 4a1 1 0 0 1 1-1h3.5a1 1 0 0 1 1 1c0 1.25.2 2.45.57 3.57a1 1 0 0 1-.25 1z"/></svg>
        <span>07312 605 227</span>
      </li>
      <li class="contact">
        <svg class="contact__icon" viewBox="0 0 24 24" aria-hidden="true"><path fill="currentColor" d="M3 5h18v14H3z"/><path d="M3 5l9 7 9-7" fill="none" stroke="#121212" stroke-width="2"/></svg>
        <span>films@lewismarrowreels.com</span>
      </li>
      <li class="contact">
        <svg class="contact__icon" viewBox="0 0 24 24" fill="none" stroke="currentColor" stroke-width="2" aria-hidden="true"><circle cx="12" cy="12" r="9"/><path d="M3 12h18M12 3c3 3 3 15 0 18M12 3c-3 3-3 15 0 18"/></svg>
        <span>www.lewismarrowreels.com</span>
      </li>
      <li class="contact" aria-label="Social page">
        <svg class="contact__icon" viewBox="0 0 24 24" aria-hidden="true"><rect x="3" y="3" width="18" height="18" rx="4" fill="currentColor"/></svg>
        <span>@lewismarrowweddingfilms</span>
      </li>
      <li class="contact" aria-label="Photo profile">
        <svg class="contact__icon" viewBox="0 0 24 24" aria-hidden="true"><circle cx="12" cy="12" r="9" fill="none" stroke="currentColor" stroke-width="2.4"/></svg>
        <span>@lewismarrowfilms</span>
      </li>
    </ul>

    <div class="emblem">
      <div class="emblem__mark"></div>
      <div class="emblem__name">LEWIS<br>MARROW</div>
    </div>
  </section>
</main>
</body>
</html>
```